Leading Nutrition Company Needs a Stylish Label Design!

We need a label/packaging design for our new cutting-edge detox called "Clear Tide". It is an all organic detox that removes toxins, harsh-chemicals, herbicides, pesticides and heavy metals from the body. It essentially turns everything you eat into organic whole foods and without all the chemicals in our bodies, we run at optimal performance.

We are attempting to blend a modern, simplistic design for our label.
We would like to see designs that use flat grays, silvers and blacks. We would also like to see pops of green and or blue in the design. Overall design will be a modern, contemporary matte finish with pops of color in either a pattern design or colored lettering. The final design should convey a high-end, exclusive health product.

Target Market(s)

Health conscious individuals and those seeking to pass an upcoming drug test. Athletes, nutritionist, dietitians ranging from 18-70 years of age.

Industry/Entity Type

Health

Font styles to use
Other font styles liked:
• Unique modern fonts

Colors
b1b1b1
9d9d9d
474747
33a6d7
0192cd
9ccb3b

Requirements
Must have
• Must be modern and simplistic

Pops of color - Don't need to be matte

Matte finishes for background
-Light grays, graphite, light silvers etc

Lettering must be modern and unique

Label type wil be a "shrink label" for an 8 oz boston squat bottle
-See attached link for bottle

"Clear Tide" some where on label

Company logo some where on label
-See attached files for logo
Nice to have
• Cool background designs that provide depth to the design.

A strip of pattern design running vertically or horizontally to capture the eye.
-See attached pictures for examples
Should not have
• Script or Normal fonts

```html
<!DOCTYPE html>
<html lang="en">
<head>
<meta charset="utf-8">
<title>Clear Tide – Label</title>
<link href="https://fonts.googleapis.com/css2?family=Quicksand:wght@500;700&family=Didact+Gothic&display=swap" rel="stylesheet">
<style>
  :root{
    --page:#ffffff;
    --graphite:#2b2b2b;
    --graphite-deep:#1f1f1f;
    --shield:#333333;
    --lime:#9ccb3b;
    --lime-bright:#a6d13f;
    --green-deep:#3d9a3c;
    --ink:#2a2a2a;
    --frame:#4a4a4a;
  }
  *{margin:0;padding:0;box-sizing:border-box}
  html,body{width:1200px;height:617px;overflow:hidden;background:var(--page)}
  .canvas{position:relative;width:1200px;height:617px;font-family:"Didact Gothic",sans-serif;color:var(--ink)}
  .dieline{position:absolute;left:88px;top:145px;width:1026px;height:368px;border:1.5px solid var(--frame)}
  .label{position:absolute;left:93px;top:103px;width:992px;height:409px;overflow:hidden;
    background:linear-gradient(180deg,var(--lime-bright) 0%,var(--lime) 62%,#7dbb39 82%,var(--green-deep) 100%)}
  .top-band{position:absolute;left:0;top:0;width:100%;height:96px;
    background:linear-gradient(180deg,var(--graphite-deep),var(--graphite))}
  .green-texture{position:absolute;left:470px;top:96px;width:522px;height:140px;
    background:linear-gradient(180deg,rgba(140,190,50,.55),rgba(156,203,59,0))}
  .shield{position:absolute;left:0;top:0}
  .brand-mark{position:absolute;display:flex;align-items:center;gap:5px;font-family:"Quicksand",sans-serif;font-weight:700;color:var(--lime);white-space:nowrap}
  .brand-mark .dot{border-radius:50%;background:currentColor;flex:none}
  .brand-front{left:220px;top:78px;font-size:10px}
  .brand-front .dot{width:12px;height:12px}
  .title{position:absolute;left:130px;top:140px;font-family:"Quicksand",sans-serif;font-weight:700;
    color:var(--lime);font-size:66px;line-height:76px;letter-spacing:3px;text-align:center;width:240px}
  .subtitle{position:absolute;left:280px;top:306px;font-size:12.5px;line-height:16px;text-align:center;font-weight:700;letter-spacing:.3px}
  .volume-front{position:absolute;left:228px;top:378px;font-family:"Quicksand",sans-serif;font-weight:700;font-size:15px}
  .volume-front small{font-size:11px}
  .back-title{position:absolute;left:672px;top:147px;font-family:"Quicksand",sans-serif;font-weight:700;font-size:21px;letter-spacing:1px;white-space:nowrap}
  .back-copy{position:absolute;left:656px;top:177px;width:162px;font-size:8px;line-height:9.6px;letter-spacing:.4px;text-align:justify}
  .contact{position:absolute;left:656px;top:254px;font-size:8px;line-height:10px;letter-spacing:.4px}
  .facts{position:absolute;left:838px;top:149px;width:124px;height:157px;overflow:hidden;background:#fff;border:1.5px solid var(--ink);padding:3px 5px;font-size:6px;line-height:6.5px}
  .facts h2{font-family:"Quicksand",sans-serif;font-size:11.5px;line-height:14px;border-bottom:3px solid var(--ink);margin-bottom:2px;white-space:nowrap}
  .facts .intake{border-bottom:1px solid var(--ink);padding-bottom:1px;margin-bottom:2px}
  .facts ul{list-style:none}
  .facts li{display:flex;justify-content:space-between;white-space:nowrap}
  .facts li span:last-child{width:30px}
  .storage{position:absolute;left:842px;top:309px;font-size:6px;white-space:nowrap}
  .brand-back{left:840px;top:332px;font-size:8px;color:var(--ink)}
  .brand-back .dot{width:14px;height:14px}
  .back-footer{position:absolute;left:846px;top:379px;font-family:"Quicksand",sans-serif;font-weight:700;font-size:12px;letter-spacing:.5px;white-space:nowrap}
  .back-footer small{font-size:9px;margin-left:4px}
</style>
</head>
<body>
<div class="canvas">
  <div class="dieline"></div>
  <div class="label">
    <div class="top-band" role="img" aria-label="Graphite band with rounded dot pattern"></div>
    <div class="green-texture" role="img" aria-label="Soft dot pattern on green"></div>
    <svg class="shield" width="500" height="360" viewBox="0 0 500 360" role="img" aria-label="Graphite shield panel with dot pattern">
      <path d="M55,0 H492 V96 C470,230 330,320 165,352 C100,300 55,230 55,140 Z" fill="var(--shield)"/>
    </svg>
    <div class="brand-mark brand-front"><span class="dot"></span>Fenwick Nutrition</div>
    <h1 class="title">CLEAR TIDE</h1>
    <p class="subtitle">Detox<br>Dietry Supplement</p>
    <p class="volume-front">8.Ø <small>oz</small></p>

    <h2 class="back-title">CLEAR TIDE</h2>
    <p class="back-copy">is an all organic detox that removes toxins, harsh-chemicals, herbicides, pesticides and heavy metals from the body. It essentially turns everything you eat into organic whole foods and without all the chemicals in our bodies, so you can function at optimal performance.</p>
    <p class="contact">Clear Tide<br>Address<br>Phone<br>Website</p>

    <div class="facts">
      <h2>Supplement Facts</h2>
      <p class="intake">DAILY INTAKE 3%</p>
      <ul>
        <li><span>NUTRITIONAL FACTS</span><span>2.0 mg</span></li>
        <li><span>NUTRITIONAL FACTS</span><span>2.0 mg</span></li>
        <li><span>NUTRITIONAL FACTS</span><span>2.0 mg</span></li>
        <li><span>NUTRITIONAL FACTS</span><span>2.0 mg</span></li>
        <li><span>NUTRITIONAL FACTS</span><span>2.0 mg</span></li>
        <li><span>NUTRITIONAL FACTS</span><span>2.0 mg</span></li>
        <li><span>NUTRITIONAL FACTS</span><span>2.0 mg</span></li>
        <li><span>NUTRITIONAL FACTS</span><span>2.0 mg</span></li>
        <li><span>NUTRITIONAL FACTS</span><span>2.0 mg</span></li>
        <li><span>NUTRITIONAL FACTS</span><span>2.0 mg</span></li>
        <li><span>NUTRITIONAL FACTS</span><span>2.0 mg</span></li>
        <li><span>NUTRITIONAL FACTS</span><span>2.0 mg</span></li>
        <li><span>NUTRITIONAL FACTS</span><span>2.0 mg</span></li>
        <li><span>NUTRITIONAL FACTS</span><span>2.0 mg</span></li>
        <li><span>NUTRITIONAL FACTS</span><span>2.0 mg</span></li>
        <li><span>NUTRITIONAL FACTS</span><span>2.0 mg</span></li>
      </ul>
    </div>
    <p class="storage">Best consumed chilled within 3-5 days.</p>
    <div class="brand-mark brand-back"><span class="dot"></span>Fenwick Nutrition</div>
    <p class="back-footer">CLEAR TIDE<small>8.Ø oz</small></p>
  </div>
</div>
</body>
</html>
```